Boutique Wealth management firm needs a new business card design

I want to update my business card design to be more consistent with the look and feel of my website (www.brisvane-wealth.com). I would like to incorporate an ivory parchment background and am open to switching from the current "portrait" layout to a more traditional "landscape" orientation. The final design should convey stability and exclusivity and I want something in PDF format that is ready to send to the printer

Thank you all for taking the time to submit your designs for my project. I've made my decision and picked the design I like best. Thanks again!

```html
<!DOCTYPE html>
<html lang="en">
<head>
<meta charset="utf-8">
<title>Brisvane Wealth Advisory – Business Card</title>
<link rel="stylesheet" href="https://fonts.googleapis.com/css2?family=Lato:wght@400;700;900&display=swap">
<style>
  :root {
    --backdrop: #2e2e30;
    --plum: #6a1f44;
    --plum-deep: #541834;
    --rule: #1a1416;
    --ink: #2a2222;
    --parchment-light: #e0c99c;
    --parchment: #d2b27c;
    --parchment-dark: #b8925c;
  }
  * { box-sizing: border-box; margin: 0; padding: 0; }
  html, body {
    width: 1200px; height: 997px; overflow: hidden;
    background: var(--backdrop);
    font-family: "Lato", Arial, sans-serif;
  }
  .sheet {
    width: 1200px; height: 997px;
    display: flex; flex-direction: column;
    align-items: center; justify-content: center; gap: 48px;
  }
  .card {
    position: relative;
    width: 760px; height: 430px;
    border-radius: 20px; overflow: hidden;
    background:
      radial-gradient(ellipse at 40% 40%, var(--parchment-light) 0%, var(--parchment) 55%, var(--parchment-dark) 100%);
    box-shadow: 0 10px 30px rgba(0,0,0,.45);
  }
  .band {
    position: absolute; left: 0; right: 0;
    background: var(--plum);
  }
  .band--top { top: 0; height: 58px; border-bottom: 6px solid var(--rule); }
  .band--bottom { bottom: 0; height: 92px; border-top: 6px solid var(--rule); background: var(--plum-deep); }
  .card--front .band--bottom { height: 78px; }

  .wordmark { color: var(--plum); font-weight: 900; text-align: center; line-height: 1; }
  .wordmark__name { display: block; letter-spacing: 2px; text-transform: uppercase; }
  .wordmark__tag { display: block; letter-spacing: .5px; margin-top: 4px; }

  .card--back .wordmark {
    position: absolute; left: 0; right: 0; top: 140px;
  }
  .card--back .wordmark__name { font-size: 74px; }
  .card--back .wordmark__tag { font-size: 34px; }

  .card--front .wordmark { position: absolute; left: 0; right: 0; top: 34px; }
  .card--front .wordmark__name { font-size: 44px; }
  .card--front .wordmark__tag { font-size: 21px; }

  .divider {
    position: absolute; left: 402px; top: 150px; width: 2px; height: 130px;
    background: linear-gradient(to bottom, transparent, var(--plum), transparent);
  }
  .person { position: absolute; left: 52px; top: 190px; }
  .person__name { color: var(--plum); font-size: 26px; font-weight: 900; letter-spacing: .5px; }
  .person__name sup { font-size: 13px; }
  .person__role { color: var(--ink); font-size: 18px; font-weight: 900; margin-top: 6px; letter-spacing: .5px; }
  .license { position: absolute; left: 52px; top: 300px; color: var(--ink); font-size: 17px; font-weight: 700; }

  .contacts { position: absolute; left: 432px; top: 128px; list-style: none; }
  .contacts li {
    display: flex; align-items: flex-start; gap: 10px;
    color: var(--ink); font-size: 16px; font-weight: 700; margin-bottom: 12px; line-height: 1.2;
  }
  .contacts svg { flex: none; width: 26px; height: 26px; margin-top: -4px; }
</style>
</head>
<body>
<main class="sheet">

  <section class="card card--back" aria-label="Card back">
    <div class="band band--top"></div>
    <div class="wordmark">
      <span class="wordmark__name">Brisvane</span>
      <span class="wordmark__tag">Wealth Advisory</span>
    </div>
    <div class="band band--bottom"></div>
  </section>

  <section class="card card--front" aria-label="Card front">
    <div class="wordmark">
      <span class="wordmark__name">Brisvane</span>
      <span class="wordmark__tag">Wealth Advisory</span>
    </div>

    <div class="person">
      <p class="person__name">DEAN HARLOW &nbsp;CFP<sup>®</sup></p>
      <p class="person__role">PRINCIPAL</p>
    </div>
    <p class="license">CA Insurance License #0K71836</p>

    <div class="divider"></div>

    <ul class="contacts">
      <li>
        <svg viewBox="0 0 26 26" aria-hidden="true"><circle cx="13" cy="13" r="13" fill="#6a1f44"/><path d="M7 10c0-2 2-3 6-3s6 1 6 3l-2 1-1-2h-6l-1 2zM8 12h10l1 7H7z" fill="#e6d2ac"/></svg>
        <span>555-014-2388</span>
      </li>
      <li>
        <svg viewBox="0 0 26 26" aria-hidden="true"><circle cx="13" cy="13" r="13" fill="#6a1f44"/><rect x="6" y="8.5" width="14" height="9.5" fill="#e6d2ac"/><path d="M6 8.5l7 5.5 7-5.5" fill="none" stroke="#6a1f44" stroke-width="1.4"/></svg>
        <span>dean@brisvane-wealth.com</span>
      </li>
      <li>
        <svg viewBox="0 0 26 26" aria-hidden="true"><circle cx="13" cy="13" r="13" fill="#6a1f44"/><g fill="none" stroke="#e6d2ac" stroke-width="2"><rect x="9" y="5.5" width="5" height="8" rx="2.5" transform="rotate(30 11.5 9.5)"/><rect x="12" y="12.5" width="5" height="8" rx="2.5" transform="rotate(30 14.5 16.5)"/></g></svg>
        <span>www.brisvane-wealth.com</span>
      </li>
      <li>
        <svg viewBox="0 0 26 26" aria-hidden="true"><circle cx="13" cy="13" r="13" fill="#6a1f44"/><path d="M13 6a5 5 0 0 1 5 5c0 4-5 9-5 9s-5-5-5-9a5 5 0 0 1 5-5z" fill="#e6d2ac"/><circle cx="13" cy="11" r="2" fill="#6a1f44"/></svg>
        <span>880 Orchard Ln. #214<br>Fairbrook, CA 94000</span>
      </li>
    </ul>

    <div class="band band--bottom"></div>
  </section>

</main>
</body>
</html>
```